Lorne Hollow Farm Postcard Design

I am looking for a new postcard design to mail out this season. We are a Farm business that does wholesale and retail and bulk seasoned firewood sales. we sell firewood from anything from bagged wood to tractor trailer loads of wood. We sell firewood in bulk bags. Pick up or delivery available there is no order to big or too small. I need my business name and phone number on the cards Lorne Hollow Farm 848-316-0572 (call or text) I would like it to say we are the best priced guaranteed. I want something that is simple and straight forward but also really catches the eye when they see these in the mail box. I attached my logo and feel free to use photos of split firewood if you would like. id like my email on the card Lornehollowfarm90@mailvista.net.

Target Market(s)

Firewood purchasers

Industry/Entity Type

agriculture

Requirements
Must have
• email phone number logo

```html
<!DOCTYPE html>
<html lang="en">
<head>
<meta charset="utf-8">
<title>Lorne Hollow Farm Postcard</title>
<link rel="stylesheet" href="https://fonts.googleapis.com/css2?family=Anton&family=Great+Vibes&family=Montserrat:wght@400;600;700;800&display=swap">
<style>
:root{
  --stage:#c9c9c9;
  --ink:#140c08;
  --yellow:#ffc400;
  --yellow-deep:#f5a800;
  --red:#ee3b24;
  --red-deep:#b3141c;
  --white:#ffffff;
  --line:#bdbdbd;
  --stamp:#e6e6e6;
}
*{box-sizing:border-box;margin:0;padding:0}
html,body{width:814px;height:1200px;overflow:hidden}
body{background:var(--stage);font-family:"Montserrat",sans-serif;position:relative;color:var(--white)}
.card{position:absolute;left:87px;width:641px;height:457px;overflow:hidden}
.front{top:119px;background:var(--ink)}
.back{top:623px;background:var(--white)}
.abs{position:absolute}

/* front */
.forest{left:0;top:0;width:641px;height:457px;background:radial-gradient(ellipse at 78% 25%,#4d4a22 0%,#2b2512 40%,#140c08 75%)}
.truck-photo{border-radius:40px 30px 20px 60px;background:linear-gradient(160deg,#9a1a24 0%,#5e0d14 55%,#2a1a14 100%)}
.brand-top{left:30px;top:20px;font-weight:800;font-size:46px;line-height:1;letter-spacing:-1px}
.brand-main{left:30px;top:64px;font-family:"Anton",sans-serif;font-size:46px;line-height:1;color:var(--yellow);letter-spacing:-.5px;transform:scaleY(1.2);transform-origin:top left;white-space:nowrap}
.brand-script{left:36px;top:116px;font-family:"Great Vibes",cursive;font-size:38px;line-height:1}
.tagline{left:30px;top:166px;width:250px;border-left:2px solid var(--yellow);padding-left:7px;font-size:10px;font-weight:600;line-height:1.2}
.perk{top:227px;width:79px;height:91px;border-radius:7px;padding:14px 4px 0;text-align:center;font-size:8.5px;line-height:1.25}
.perk b{font-weight:700}
.perk-red{background:linear-gradient(180deg,var(--red),#ff5a2a)}
.perk-yellow{background:linear-gradient(180deg,var(--yellow),var(--yellow-deep));color:var(--ink)}
.perk-icon{top:203px;width:32px;height:32px;border-radius:50%;background:var(--ink);border:2px solid var(--red);display:flex;align-items:center;justify-content:center}
.perk-icon.gold{border-color:var(--yellow)}
.badge{border-radius:50%;background:radial-gradient(circle at 40% 35%,#d9262b,var(--red-deep));text-align:center;display:flex;flex-direction:column;align-items:center;justify-content:center;box-shadow:0 0 0 2px #e3342c}
.badge .small{font-weight:700;line-height:1}
.badge .big{font-family:"Anton",sans-serif;color:var(--yellow);line-height:1}
.badge .big.white{color:var(--white)}
.badge .stars{color:var(--yellow);line-height:1}
.farm-name{font-weight:800;color:var(--yellow);text-align:center;line-height:1.1;display:flex;flex-direction:column;align-items:center;gap:4px}
.farm-dot{width:10px;height:10px;border-radius:50%;background:var(--red)}
.cta-label{font-weight:800;color:var(--yellow);display:flex;align-items:center;gap:4px;line-height:1}
.cta-or{width:13px;height:13px;border-radius:50%;background:var(--red);color:var(--white);font-size:7px;display:inline-flex;align-items:center;justify-content:center;font-weight:600}
.contact{font-weight:700;display:flex;align-items:center;gap:5px;line-height:1;white-space:nowrap}
.ico{border-radius:50%;background:var(--red);display:inline-flex;align-items:center;justify-content:center;flex:none}
.divider{left:355px;top:392px;height:44px;border-left:1px dashed var(--white)}

/* back */
.back-panel{left:0;top:0;width:364px;height:457px;background:radial-gradient(ellipse at 60% 90%,#3a2718 0%,var(--ink) 65%)}
.back-kicker{left:29px;top:27px;font-size:11px;font-weight:800;color:var(--yellow);white-space:nowrap}
.back-title{left:29px;top:44px;font-family:"Anton",sans-serif;font-size:26px;line-height:1.08;letter-spacing:-.5px;transform:scaleY(1.2);transform-origin:top left;white-space:nowrap}
.back-truck{left:202px;top:23px;width:157px;height:125px;border-radius:30px 20px 40px 40px;background:linear-gradient(160deg,#8c1a22,#4b0d12 60%,#26201c)}
.band{left:0;top:135px;width:376px;height:156px;background:linear-gradient(180deg,var(--yellow),var(--yellow-deep))}
.tab{left:0;top:123px;width:154px;height:19px;background:var(--red);border-radius:0 10px 10px 0;font-weight:800;font-size:11px;letter-spacing:2px;color:var(--white);padding-left:29px;line-height:19px}
.services{list-style:none;color:var(--ink);font-size:10px;font-weight:600}
.services li{display:flex;align-items:flex-start;gap:5px;height:18px;line-height:1.15}
.services li::before{content:"";width:7px;height:7px;border-radius:50%;background:var(--red);margin-top:3px;flex:none}
.services li.tall{height:30px}
.more{left:163px;top:221px;font-weight:800;font-size:10px;color:var(--red)}
.col-rule{left:144px;top:158px;height:92px;border-left:1px solid rgba(0,0,0,.12)}
.gallery{left:30px;top:257px;width:304px;height:81px;background:var(--white);padding:3px;display:flex;gap:4px}
.gallery div{flex:1}
.stamp{left:540px;top:29px;width:71px;height:71px;border-radius:5px;background:var(--stamp)}
.addr-line{left:411px;width:200px;border-top:1px solid var(--line)}
</style>
</head>
<body>

<section class="card front">
  <div class="abs forest" role="img" aria-label="Dark forest background with tall tree trunks"></div>
  <div class="abs truck-photo" style="left:271px;top:66px;width:370px;height:307px" role="img" aria-label="Photo of the farm's red semi truck"></div>

  <div class="abs brand-top">Lorne</div>
  <div class="abs brand-main">HOLLOW FARM</div>
  <div class="abs brand-script">Tree service</div>
  <p class="abs tagline">We are a Farm business that does wholesale and retail and bulk seasoned firewood sales</p>

  <div class="abs perk perk-red" style="left:31px">we sell <b>firewood</b> from anything from <b>bagged wood to tractor trailer loads of wood</b></div>
  <div class="abs perk perk-yellow" style="left:113px"><b>Pick up or delivery available</b> there is no order to big or too small</div>
  <div class="abs perk perk-red" style="left:195px">We sell <b>firewood in bulk bags</b></div>

  <div class="abs perk-icon" style="left:55px">
    <svg width="14" height="14" viewBox="0 0 14 14" fill="none" stroke="#fff" stroke-width="1.2"><circle cx="8" cy="5" r="3.5"/><path d="M1 12h4l3-2h4"/><path d="M8 3.5v3"/></svg>
  </div>
  <div class="abs perk-icon gold" style="left:137px">
    <svg width="16" height="12" viewBox="0 0 16 12" fill="none" stroke="#fff" stroke-width="1.2"><rect x="1" y="2" width="9" height="6"/><path d="M10 4h3l2 2v2h-5"/><circle cx="4" cy="10" r="1.3"/><circle cx="12" cy="10" r="1.3"/></svg>
  </div>
  <div class="abs perk-icon" style="left:219px">
    <svg width="16" height="12" viewBox="0 0 16 12" fill="none" stroke="#fff" stroke-width="1.2"><circle cx="4" cy="8" r="3"/><circle cx="11" cy="8" r="3"/><circle cx="7.5" cy="3.5" r="2.5"/></svg>
  </div>

  <div class="abs badge" style="left:303px;top:72px;width:98px;height:98px">
    <span class="small" style="font-size:9px">we are the</span>
    <span class="big" style="font-size:17px">BEST PRICED</span>
    <span class="big white" style="font-size:17px">GUARANTEED</span>
    <span class="stars" style="font-size:11px">★★★</span>
  </div>

  <div class="abs farm-name" style="left:30px;top:360px;width:100px;font-size:13px">
    <span class="farm-dot"></span>
    <span>Lorne Hollow Farm</span>
  </div>

  <div class="abs cta-label" style="left:162px;top:391px;font-size:14px">CALL <span class="cta-or">or</span> TEXT</div>
  <div class="abs contact" style="left:162px;top:412px;font-size:19px">
    <span class="ico" style="width:15px;height:15px"><svg width="9" height="9" viewBox="0 0 10 10"><path d="M2 1l2 2-1 1.5c.6 1.2 1.3 1.9 2.5 2.5L7 6l2 2-1.5 1.5C4.5 9 1 5.5.5 2.5z" fill="#fff"/></svg></span>
    848-316-0572
  </div>
  <div class="abs divider"></div>
  <div class="abs cta-label" style="left:385px;top:391px;font-size:14px">EMAIL US AT</div>
  <div class="abs contact" style="left:385px;top:415px;font-size:11.5px;font-weight:600">
    <span class="ico" style="width:13px;height:13px"><svg width="8" height="6" viewBox="0 0 8 6" fill="none" stroke="#fff" stroke-width=".9"><rect x=".5" y=".5" width="7" height="5"/><path d="M.5.5l3.5 3 3.5-3"/></svg></span>
    Lornehollowfarm90@mailvista.net
  </div>
</section>

<section class="card back">
  <div class="abs back-panel"></div>
  <div class="abs back-kicker">TREE REMOVAL, PRUNING</div>
  <div class="abs back-title">STUMP GRINDING<br>&amp; LANDSCAPING</div>

  <div class="abs band"></div>
  <div class="abs back-truck" role="img" aria-label="Photo of the farm's red semi truck"></div>
  <div class="abs tab">OUR SERVICES</div>

  <ul class="abs services" style="left:30px;top:160px">
    <li>Tree removal</li>
    <li>Tree trimming</li>
    <li>Stump grinding</li>
    <li>Stone</li>
    <li>Mulch</li>
  </ul>
  <div class="abs col-rule"></div>
  <ul class="abs services" style="left:163px;top:160px">
    <li class="tall">Spring<br>clean ups</li>
    <li>Gravel</li>
    <li>Landscaping</li>
  </ul>
  <div class="abs more">And much more</div>

  <div class="abs badge" style="left:268px;top:158px;width:66px;height:66px">
    <span class="small" style="font-size:6.5px">we are the</span>
    <span class="big" style="font-size:11.5px">BEST PRICED</span>
    <span class="big white" style="font-size:11.5px">GUARANTEED</span>
    <span class="stars" style="font-size:8px">★★★</span>
  </div>

  <div class="abs gallery">
    <div role="img" aria-label="Photo of tree removal equipment in a wooded yard" style="background:linear-gradient(180deg,#8a8a86,#5c5047)"></div>
    <div role="img" aria-label="Photo of a worker lifting a log beside a wood chipper" style="background:linear-gradient(180deg,#9fb0b8,#6b4b52)"></div>
    <div role="img" aria-label="Photo of cut log rounds stacked on a trailer" style="background:linear-gradient(180deg,#8e8b80,#4a3a2c)"></div>
  </div>

  <div class="abs farm-name" style="left:27px;top:375px;width:84px;font-size:11px">
    <span class="farm-dot"></span>
    <span>Lorne Hollow Farm</span>
  </div>

  <div class="abs cta-label" style="left:128px;top:374px;font-size:14px">CALL <span class="cta-or">or</span> TEXT</div>
  <div class="abs contact" style="left:128px;top:396px;font-size:17px">
    <span class="ico" style="width:13px;height:13px"><svg width="8" height="8" viewBox="0 0 10 10"><path d="M2 1l2 2-1 1.5c.6 1.2 1.3 1.9 2.5 2.5L7 6l2 2-1.5 1.5C4.5 9 1 5.5.5 2.5z" fill="#fff"/></svg></span>
    848-316-0572
  </div>
  <div class="abs contact" style="left:128px;top:420px;font-size:10.5px;font-weight:600">
    <span class="ico" style="width:13px;height:13px"><svg width="8" height="6" viewBox="0 0 8 6" fill="none" stroke="#fff" stroke-width=".9"><rect x=".5" y=".5" width="7" height="5"/><path d="M.5.5l3.5 3 3.5-3"/></svg></span>
    Lornehollowfarm90@mailvista.net
  </div>

  <div class="abs stamp"></div>
  <div class="abs addr-line" style="top:249px"></div>
  <div class="abs addr-line" style="top:286px"></div>
  <div class="abs addr-line" style="top:322px"></div>
</section>

</body>
</html>
```